Pale Lanterns Old Lane Walk Poster Design

We need an A4 sized poster to promote our weekly true crime tours. This poster will be posted onto community noticeboards.
Lots of information and images can be viewed at the following links:-
www.palelanterns.com.au
www.palelanterns.com.au/bookings/
https://www.facebook.com/palelanternsoldlane/
https://www.examplereviews.com.au/Attraction_Review-g000000-d00000000-Reviews-Pale_Lanterns-Newcastle_Greater_Newcastle_New_South_Wales.html
There are also a number of images for possible use at the following link - we are open to intepretation:-
http://palelanterns.com.au/tour-photographs/
The font on our website is "SpecialElite" so we would like to continue using that font type.
Target Market(s)
Adults 25-65.
Font styles to use
Other font styles liked:
- Special Elite
Colors
Designer to choose colors to be used in the design.
Look and feel
Each slider illustrates characteristics of the customer's brand and the style your logo design should communicate.

```html
<!DOCTYPE html>
<html lang="en">
<head>
<meta charset="utf-8">
<title>Pale Lanterns Old Lane Walk</title>
<link rel="stylesheet" href="https://fonts.googleapis.com/css2?family=Special+Elite&family=Poppins:wght@400;600&display=swap">
<style>
  :root {
    --red: #e1252b;
    --white: #ffffff;
    --ink: #1b1b1b;
    --paper-dark: #262626;
    --text-soft: #eeeeee;
  }
  * { margin: 0; padding: 0; box-sizing: border-box; }
  html, body { width: 849px; height: 1200px; overflow: hidden; background: var(--ink); }
  .poster {
    position: relative;
    width: 849px;
    height: 1200px;
    overflow: hidden;
    background: linear-gradient(180deg, #3a3a3a 0%, #2e2e2e 50%, #242424 75%, #1e1e1e 100%);
    color: var(--white);
    font-family: "Poppins", sans-serif;
  }
  .street-photo {
    position: absolute;
    left: 0; top: 0;
    width: 849px; height: 560px;
    background:
      radial-gradient(ellipse at 40% 55%, #8c8c8c 0%, #5e5e5e 35%, rgba(50,50,50,0) 75%),
      linear-gradient(180deg, #4a4a4a 0%, #6d6d6d 45%, #555 70%, #2f2f2f 100%);
  }
  .title-bar {
    position: absolute;
    background: var(--red);
    font-family: "Special Elite", monospace;
    font-weight: 400;
    color: var(--white);
    line-height: 1;
    white-space: nowrap;
    overflow: hidden;
  }
  .title-bar--first { left: 18px; top: 32px; width: 552px; height: 64px; font-size: 56px; padding: 5px 0 0 14px; }
  .title-bar--second { left: 193px; top: 100px; width: 645px; height: 78px; font-size: 64px; padding: 7px 0 0 14px; }
  .tagline {
    position: absolute;
    right: 14px; top: 186px;
    font-family: "Special Elite", monospace;
    font-size: 24px;
    white-space: nowrap;
  }
  .headline {
    position: absolute;
    left: 30px; top: 548px;
    font-family: "Special Elite", monospace;
    font-weight: 400;
    font-size: 34px;
    line-height: 42px;
    text-transform: uppercase;
    white-space: nowrap;
  }
  .highlights {
    position: absolute;
    left: 20px; top: 622px;
    list-style: none;
    font-size: 16.5px;
    color: var(--text-soft);
  }
  .highlights li { height: 43px; display: flex; align-items: center; white-space: nowrap; }
  .highlights li::before {
    content: "";
    width: 7px; height: 7px;
    background: var(--red);
    margin-right: 8px;
    flex: none;
  }
  .rule { position: absolute; left: 30px; top: 834px; width: 792px; height: 2px; background: var(--red); }
  .price {
    position: absolute;
    left: 44px; top: 850px;
    font-family: "Special Elite", monospace;
    font-size: 58px;
    white-space: nowrap;
  }
  .facts { position: absolute; left: 298px; top: 852px; font-size: 25px; line-height: 42px; white-space: nowrap; }
  .facts .label { color: var(--red); font-weight: 600; }
  .promise {
    position: absolute;
    left: 165px; top: 948px;
    width: 667px; height: 66px;
    background: var(--red);
    font-family: "Special Elite", monospace;
    font-size: 35px;
    display: flex; align-items: center; justify-content: center;
    white-space: nowrap;
    overflow: hidden;
  }
  .meeting {
    position: absolute;
    left: 60px; top: 1028px;
    width: 766px;
    text-align: right;
    font-size: 16px;
    line-height: 30px;
    color: var(--text-soft);
  }
  .brand {
    position: absolute;
    left: 0; top: 1090px;
    width: 262px; height: 110px;
    background: var(--paper-dark);
    display: flex; align-items: center; justify-content: center; gap: 10px;
    font-family: "Special Elite", monospace;
    font-size: 26px;
    white-space: nowrap;
  }
  .brand-mark { width: 14px; height: 14px; background: var(--white); flex: none; }
  .website {
    position: absolute;
    left: 268px; top: 1160px;
    font-size: 19px;
    font-weight: 600;
    letter-spacing: 0.5px;
    white-space: nowrap;
  }
  .bookings {
    position: absolute;
    right: 28px; top: 1112px;
    text-align: center;
    font-family: "Special Elite", monospace;
    font-size: 32px;
    line-height: 34px;
    color: var(--red);
    white-space: nowrap;
  }
</style>
</head>
<body>
<main class="poster">
  <div class="street-photo" role="img" aria-label="Black and white photograph of a tram on a rainy city street at night with a lone pedestrian"></div>

  <h1>
    <span class="title-bar title-bar--first">Pale Lanterns</span>
    <span class="title-bar title-bar--second">Old Lane Walk</span>
  </h1>
  <p class="tagline">stories the city tried to forget</p>

  <h2 class="headline">Take a walk on the dark side -<br>revisit the scenes of the crimes.</h2>

  <ul class="highlights">
    <li>Retrace the steps of Newcastle's most infamous murderers.</li>
    <li>Descend into the murky world of fraudsters, adulterers and lordly impersonators.</li>
    <li>Unearth the keys to the heart of the Lamplight Killer.</li>
    <li>Relive a time that proves truth is far stranger than fiction.</li>
    <li>Book your ticket for a unique investigation into a dark and crime ridden history.</li>
  </ul>

  <div class="rule"></div>

  <p class="price">$34.00</p>
  <p class="facts">
    <span class="label">Duration:</span> 90 Minutes (approx.)<br>
    <span class="label">Location:</span> Newcastle East, NSW
  </p>

  <p class="promise">100% TRUE - 100% UNBELIEVABLE</p>

  <p class="meeting">Meets at the corner of Harbour Rd &amp; Bell St, Newcastle; adjacent to the Old Wharf House<br>and the Stone Yard.&nbsp; Bring comfortable shoes.</p>

  <div class="brand"><span class="brand-mark"></span>Pale Lanterns</div>
  <p class="website">www.palelanterns.com.au</p>
  <p class="bookings">BOOKINGS<br>ESSENTIAL.</p>
</main>
</body>
</html>
```